Buchcover-Design für Science-Fiction-Roman
Zielgruppe
Ich habe einen Science-Fiction-Roman geschrieben und benötige dafür ein Buchcover.
Meine Zielgruppe sind Leser- und Leserinnen ab 18, Science-Fiction-Fans.
Aufgabenstellung
Zur Einstimmung und Orientierung habe ich ein kurzes Exposé und eine Leseprobe des Romans hochgeladen.
Für das Cover stelle ich mir etwas Dezentes aber trotzdem künstlerisch Anspruchsvolles vor, gerne auch abstrakt.
Es sollte der Titel (Unter Glas), meine Name (Lenor Vasić) und 'Roman' auf dem Cover.
Den genauen Klappentext reiche ich noch nach.
Das Format ist 12,7 x 20,32 cm (5 x 8 Zoll), Rückenbreite etwa 2 cm.

```html
<!DOCTYPE html>
<html lang="de">
<head>
<meta charset="utf-8">
<title>Unter Glas – Buchumschlag</title>
<link href="https://fonts.googleapis.com/css2?family=Anton&family=Barlow:wght@400;500;600&display=swap" rel="stylesheet">
<style>
  :root {
    --paper: #ffffff;
    --amber-top: #a86b20;
    --amber-mid: #d49a12;
    --amber-low: #e4b72a;
    --rust: #963f18;
    --umber: #5e2c14;
    --ink: #4a2410;
    --author-yellow: #f5e21a;
    --silhouette: #560f12;
    --rule: #f3e3a8;
  }
  * { margin: 0; padding: 0; box-sizing: border-box; }
  html, body { width: 1200px; height: 889px; overflow: hidden; background: var(--paper); }
  .canvas { position: relative; width: 1200px; height: 889px; background: var(--paper); }

  .panel {
    position: absolute; top: 32px; height: 821px; overflow: hidden;
    background: linear-gradient(180deg, var(--amber-top) 0%, var(--amber-mid) 38%, var(--amber-low) 100%);
  }
  .back-cover  { left: 47px;  width: 513px; }
  .spine       { left: 560px; width: 81px; border-left: 1px solid var(--rule); border-right: 1px solid var(--rule); }
  .front-cover { left: 641px; width: 513px; }

  .title-word { font-family: "Anton", sans-serif; line-height: 1; text-transform: uppercase; }
  .back-title { position: absolute; left: 39px; top: 70px; }
  .back-title .line-one { color: var(--rust); font-size: 100px; transform: scaleY(0.85); transform-origin: top left; display: block; }
  .back-title .line-two { color: var(--umber); font-size: 100px; transform: scaleY(0.85); transform-origin: top left; display: block; margin-top: -2px; letter-spacing: 2px; }

  .blurb {
    position: absolute; left: 39px; top: 278px; width: 428px;
    font-family: "Barlow", sans-serif; font-size: 14.4px; line-height: 18.8px; color: var(--ink);
  }
  .code-field { position: absolute; left: 271px; top: 664px; width: 202px; height: 122px; background: var(--paper); }

  .spine-title, .spine-author {
    position: absolute; left: 50%; font-family: "Barlow", sans-serif; font-weight: 500;
    color: var(--umber); white-space: nowrap; writing-mode: vertical-rl; transform: translateX(-50%) rotate(180deg);
  }
  .spine-title { top: 36px; font-size: 28px; letter-spacing: 1px; }
  .spine-author { bottom: 34px; font-size: 28px; }
  .spine-figure { position: absolute; left: 2px; top: 255px; width: 76px; height: 178px; }

  .clock-art { position: absolute; left: 241px; top: 0; width: 272px; height: 324px; }
  .skyline-art { position: absolute; left: 0; top: 508px; width: 513px; height: 313px; }
  .front-figure { position: absolute; left: 368px; top: 255px; width: 84px; height: 178px; }

  .front-author {
    position: absolute; left: 173px; top: 48px;
    font-family: "Barlow", sans-serif; font-weight: 500; font-size: 27px; color: var(--author-yellow);
  }
  .front-title-top {
    position: absolute; left: 172px; top: 96px; width: 164px;
    color: var(--rust); font-size: 64px; letter-spacing: 1px;
    transform: scaleY(2.15); transform-origin: top left;
  }
  .front-title-main {
    position: absolute; left: 172px; top: 250px; width: 164px; height: 524px;
    color: var(--umber); font-size: 214px; line-height: 164px;
    writing-mode: vertical-rl; text-align: center; letter-spacing: 6px;
  }
  .front-genre {
    position: absolute; left: 174px; top: 778px;
    font-family: "Barlow", sans-serif; font-size: 15px; letter-spacing: 0.3px; color: var(--ink);
  }
</style>
</head>
<body>
<div class="canvas">

  <section class="panel back-cover">
    <h2 class="back-title">
      <span class="title-word line-one">Unter</span>
      <span class="title-word line-two">Glas</span>
    </h2>
    <p class="blurb">Lorem ipsum dolor sit amet, consectetuer adipiscing elit. Aenean commodo ligula eget dolor. Aenean massa. Cum sociis natoque penatibus et magnis dis parturient montes, nascetur ridiculus mus. Donec quam felis, ultricies nec, pellentesque eu, pretium quis, sem. Nulla consequat massa quis enim. Donec pede justo, fringilla vel, aliquet nec, vulputate eget, arcu. In enim justo, rhoncus ut, imperdiet a, venenatis vitae, justo. Nullam dictum felis eu pede mollis pretium. Integer tincidunt. Cras dapibus. Vivamus elementum semper nisi. Aenean vulputate eleifend tellus. Aenean leo ligula, porttitor eu, consequat vitae, eleifend ac, enim. Aliquam lorem ante, dapibus in, viverra quis, feugiat a, tellus.</p>
    <div class="code-field"></div>
  </section>

  <section class="panel spine">
    <div class="spine-title">UNTER GLAS</div>
    <svg class="spine-figure" role="img" aria-label="Silhouette einer kopfüber fallenden Person" viewBox="0 0 76 178">
      <rect x="22" y="0" width="32" height="178" rx="14" fill="var(--silhouette)" opacity="0.85"/>
    </svg>
    <div class="spine-author">Lenor Vasić</div>
  </section>

  <section class="panel front-cover">
    <svg class="clock-art" role="img" aria-label="Verblasstes Ziffernblatt einer großen Uhr mit römischen Zahlen" viewBox="0 0 272 324">
      <defs>
        <radialGradient id="clockGlow" cx="0.85" cy="0.15" r="0.9">
          <stop offset="0" stop-color="#7a4a1c" stop-opacity="0.75"/>
          <stop offset="1" stop-color="#a8701f" stop-opacity="0"/>
        </radialGradient>
      </defs>
      <rect width="272" height="324" fill="url(#clockGlow)"/>
    </svg>
    <svg class="skyline-art" role="img" aria-label="Blasse Hochhaussilhouetten einer Großstadt" viewBox="0 0 513 313">
      <defs>
        <linearGradient id="skylineFade" x1="0" y1="0" x2="0" y2="1">
          <stop offset="0" stop-color="#e0b440" stop-opacity="0"/>
          <stop offset="0.3" stop-color="#d8ab3c" stop-opacity="0.55"/>
          <stop offset="1" stop-color="#d3a43a" stop-opacity="0.7"/>
        </linearGradient>
      </defs>
      <rect width="513" height="313" fill="url(#skylineFade)"/>
    </svg>
    <svg class="front-figure" role="img" aria-label="Silhouette einer kopfüber fallenden Person" viewBox="0 0 84 178">
      <rect x="24" y="0" width="36" height="178" rx="16" fill="var(--silhouette)" opacity="0.85"/>
    </svg>

    <div class="front-author">Lenor Vasić</div>
    <h1>
      <span class="title-word front-title-top">Unter</span>
      <span class="title-word front-title-main">Glas</span>
    </h1>
    <div class="front-genre">Science Fiction Roman</div>
  </section>

</div>
</body>
</html>
```